Exceptional Corporate Business Card Design

Hello,

We need an exceptional corporate business card design based on our logo attached. We require:

1. A Variation for letterpress print
2. Standard size of business card 84mm x 55mm (Artwork 88mm x 59mm)
3. Variation for square business card 65mm x 65mm (Artwork 69mm x 69mm)
4. Variation as a one side print
5. Adobe Illustrator files

The company is in the financial industry, dulvant.com

The logo is attached as vector pdf.
regards

```html
<!DOCTYPE html>
<html lang="en">
<head>
<meta charset="UTF-8">
<title>Dulvant – Business Card</title>
<link href="https://fonts.googleapis.com/css2?family=EB+Garamond:wght@400;600&display=swap" rel="stylesheet">
<style>
  :root {
    --brand-blue: #2f2d86;
    --card-white: #ffffff;
    --stage: #e9e6e1;
    --shadow: rgba(0, 0, 0, 0.18);
  }
  * { margin: 0; padding: 0; box-sizing: border-box; }
  html, body {
    width: 1200px; height: 800px; overflow: hidden;
    background: var(--stage);
    font-family: "EB Garamond", Georgia, serif;
  }
  .stage {
    position: relative; width: 1200px; height: 800px;
    display: flex; align-items: center; justify-content: center; gap: 60px;
  }
  .card {
    position: relative; width: 500px; height: 327px;
    background: var(--card-white);
    box-shadow: 0 8px 24px var(--shadow);
    overflow: hidden;
  }

  /* Front: blue bands on top and bottom */
  .band {
    position: absolute; left: 0; right: 0; height: 46px;
    background: var(--brand-blue);
  }
  .band::after {
    content: ""; position: absolute; left: 0; right: 0; height: 5px;
    background: var(--card-white);
  }
  .band--top { top: 0; }
  .band--top::after { bottom: 5px; }
  .band--bottom { bottom: 0; }
  .band--bottom::after { top: 5px; }

  .wordmark {
    position: absolute; display: flex; align-items: center; gap: 14px;
    color: var(--brand-blue);
  }
  .wordmark__dot {
    width: 56px; height: 56px; border-radius: 50%;
    background: var(--brand-blue); flex: none;
  }
  .wordmark__name {
    font-weight: 600; font-size: 58px; line-height: 1; letter-spacing: 1px;
  }
  .card--front .wordmark { left: 50%; top: 50%; transform: translate(-50%, -50%); }

  /* Back: blue upper panel with contact, white lower panel with name mark */
  .contact-panel {
    position: absolute; left: 0; right: 0; top: 0; height: 178px;
    background: var(--brand-blue);
    color: var(--card-white);
    padding: 20px 40px 0 0;
    text-align: right;
  }
  .divider {
    position: absolute; left: 0; right: 0; top: 178px; height: 10px;
    background: var(--brand-blue);
  }
  .divider::before {
    content: ""; position: absolute; left: 0; right: 0; top: 0; height: 4px;
    background: var(--card-white);
  }
  .person__name { font-size: 24px; font-weight: 600; line-height: 1.1; }
  .person__role { font-size: 11px; line-height: 1.3; margin-top: 2px; }
  .contact-list { list-style: none; margin-top: 16px; font-size: 13px; line-height: 1.4; }
  .card--back .wordmark { left: 50%; top: 258px; transform: translate(-50%, -50%); }
  .card--back .wordmark__name { font-size: 46px; }
  .card--back .wordmark__dot { width: 44px; height: 44px; }
</style>
</head>
<body>
  <main class="stage">
    <section class="card card--front" aria-label="Card front">
      <div class="band band--top"></div>
      <div class="wordmark">
        <span class="wordmark__dot"></span>
        <span class="wordmark__name">Dulvant</span>
      </div>
      <div class="band band--bottom"></div>
    </section>

    <section class="card card--back" aria-label="Card back">
      <div class="contact-panel">
        <p class="person__name">Adrian Hale</p>
        <p class="person__role">Project Manager</p>
        <ul class="contact-list">
          <li>www.dulvant.com</li>
          <li>office@dulvant.com</li>
          <li>14-16 Ferris Lane, NW3 2QT,<br>London, England</li>
        </ul>
      </div>
      <div class="divider"></div>
      <div class="wordmark">
        <span class="wordmark__dot"></span>
        <span class="wordmark__name">Dulvant</span>
      </div>
    </section>
  </main>
</body>
</html>
```